Professional Learning Organization for Educators needs a Design Thinking Workshop Flyer

We need a flyer for a series of Introductory Design Thinking workshops we're delivering for education leaders.

We have generated our own version of the flyer with a word template, but want it to look even more professional and eye catching. It is attached.

We had an image that we thought might be good, but pulled it out so we don't bias designers' thinking.

Reason: We are a bit flexible on the deadline since this is a holiday week and people are traveling

Target Market(s)

Very busy education leaders whose curiosity needs to be stimulated enough to enroll in the course

Industry/Entity Type

Education

Font styles to use
Other font styles liked:
• Century Gothic or something closer to that

Requirements
Must have
• Some version of the text that is on the current flyer that I attached.
Nice to have
• I am very flexible and open right now on this design.

```html
<!DOCTYPE html>
<html lang="en">
<head>
<meta charset="utf-8">
<title>Design Thinking Workshops Flyer</title>
<link href="https://fonts.googleapis.com/css2?family=Questrial&family=Poppins:ital,wght@0,500;0,600;0,700;1,500;1,600;1,700;1,800&display=swap" rel="stylesheet">
<style>
  :root {
    --page-bg: #ececec;
    --paper: #ffffff;
    --ink: #2b2b2b;
    --accent-red: #e02a26;
    --red-deep: #c81d1b;
    --red-text: #e8312c;
    --green: #5fb536;
    --green-dark: #3f8f22;
    --blue: #2a62b8;
    --blue-light: #3f7fd6;
    --band-gray: #555555;
    --photo-light: #e9ecef;
    --photo-mid: #c9ced6;
  }
  * { box-sizing: border-box; margin: 0; padding: 0; }
  html, body { width: 1200px; height: 1200px; overflow: hidden; }
  body {
    background: var(--page-bg);
    font-family: "Questrial", "Century Gothic", sans-serif;
    color: var(--ink);
  }
  .flyer {
    position: absolute;
    left: 190px; top: 60px;
    width: 820px; height: 1080px;
    background: var(--paper);
    overflow: hidden;
    box-shadow: 0 10px 30px rgba(0,0,0,.18);
  }
  .hero-photo {
    position: absolute; left: 0; top: 0; width: 820px; height: 330px;
    background: linear-gradient(180deg, var(--photo-light) 0%, var(--photo-mid) 100%);
  }
  .hero-shapes { position: absolute; left: 0; top: 0; }
  .title-banner {
    position: absolute; left: 90px; top: 240px; width: 760px; height: 66px;
    background: linear-gradient(180deg, #78c84a, var(--green) 60%, var(--green-dark));
    transform: rotate(-1.5deg);
    box-shadow: 0 4px 8px rgba(0,0,0,.25);
    display: flex; align-items: center; padding-left: 40px;
  }
  .title-banner h1 {
    font-family: "Poppins", sans-serif; font-weight: 800; font-style: italic;
    color: #fff; font-size: 40px; letter-spacing: 1px; text-transform: uppercase;
  }
  .tagline {
    position: absolute; left: 0; top: 330px; width: 470px; height: 36px;
    background: var(--blue);
    color: #fff; font-family: "Poppins", sans-serif; font-weight: 600; font-style: italic;
    font-size: 17px; display: flex; align-items: center; padding-left: 30px;
  }
  .details {
    position: absolute; left: 40px; top: 390px; width: 410px;
    font-size: 14.5px; line-height: 1.4;
  }
  .details .intro { text-align: justify; margin-bottom: 12px; }
  .details ul { list-style: none; margin-bottom: 14px; }
  .details li { position: relative; padding-left: 22px; margin-bottom: 6px; }
  .details li::before {
    content: ""; position: absolute; left: 4px; top: 7px;
    width: 7px; height: 7px; border-radius: 50%; background: var(--ink);
  }
  .goals li { font-family: "Poppins", sans-serif; font-weight: 600; font-size: 13.5px; }
  .schedule li { font-family: "Poppins", sans-serif; font-weight: 600; font-size: 13.5px; margin-bottom: 4px; }
  .schedule .day { color: var(--red-text); font-weight: 500; }
  .location { font-family: "Poppins", sans-serif; font-weight: 600; font-size: 13.5px; }
  .location .label { color: var(--red-text); font-weight: 500; }
  .fee {
    display: inline-block; margin-top: 6px; background: var(--blue);
    color: #fff; font-size: 14px; padding: 3px 14px 3px 8px;
  }
  .fee strong { font-family: "Poppins", sans-serif; font-weight: 600; font-size: 16px; }
  .enroll-band {
    position: absolute; left: 0; top: 990px; width: 480px; height: 90px;
    background: linear-gradient(180deg, #6a6a6a, var(--band-gray));
    color: #fff; font-size: 15px; display: flex; align-items: center; padding-left: 22px;
  }
  .testimonials {
    position: absolute; left: 430px; top: 430px; width: 390px; height: 650px;
    background: linear-gradient(180deg, var(--accent-red), var(--red-deep));
    clip-path: polygon(90px 0, 100% 0, 100% 100%, 0 100%);
  }
  .testimonials-label {
    position: absolute; left: 505px; top: 445px; width: 315px; height: 36px;
    background: linear-gradient(180deg, #78c84a, var(--green));
    color: var(--ink); font-family: "Poppins", sans-serif; font-style: italic; font-weight: 600;
    font-size: 16px; display: flex; align-items: center; padding-left: 18px;
  }
  .quotes {
    position: absolute; left: 530px; top: 505px; width: 268px; color: #fff;
  }
  .quotes blockquote {
    font-family: "Poppins", sans-serif; font-style: italic; font-weight: 500;
    font-size: 13px; line-height: 1.4; margin-bottom: 26px; text-align: justify;
  }
  .quotes blockquote::before { content: "\201C"; font-size: 22px; line-height: 0; margin-right: 2px; }
  .quotes blockquote::after { content: "\201D"; font-size: 22px; line-height: 0; margin-left: 2px; }
  .contact {
    position: absolute; left: 500px; top: 885px; width: 300px; color: #fff;
    font-family: "Poppins", sans-serif;
  }
  .contact .org { font-weight: 700; font-style: italic; font-size: 20px; text-transform: uppercase; }
  .contact .web { font-weight: 600; font-size: 15px; margin: 4px 0 12px; }
  .contact .ask { font-weight: 700; font-style: italic; font-size: 21px; }
  .contact .email { font-weight: 600; font-size: 15px; margin-top: 2px; }
</style>
</head>
<body>
  <article class="flyer">
    <div class="hero-photo" role="img" aria-label="Photo of smiling education leaders gathered around a meeting table with charts"></div>
    <svg class="hero-shapes" width="820" height="360" viewBox="0 0 820 360" aria-hidden="true">
      <polygon points="0,130 140,110 70,330 0,330" fill="var(--blue-light)"/>
      <polygon points="0,150 120,135 60,330 0,330" fill="var(--blue)"/>
      <polygon points="820,250 820,330 560,330" fill="var(--blue)"/>
      <polygon points="0,330 820,300 820,345 0,345" fill="#ffffff"/>
    </svg>

    <div class="title-banner"><h1>Design Thinking Workshops</h1></div>
    <div class="tagline">Designing your way to better solutions</div>

    <section class="details">
      <p class="intro">Ridgeview Public Schools and Summit Valley BOCES invite you to discover the power of Design Thinking. During our three session course, you will learn and practice mindsets and tools that help you continuously and creatively improve the experiences of the people you serve by:</p>
      <ul class="goals">
        <li>Understanding what your teachers, students and community truly need in their learning and work experiences.</li>
        <li>Designing solutions that better meet their needs.</li>
        <li>Seeking authentic feedback and reactions to these solutions prior to their implementation.</li>
      </ul>
      <p class="intro">We are offering this three-session course at four different times in spring semester. Please choose the course that works best for your schedule.</p>
      <ul class="schedule">
        <li><span class="day">Monday mornings:</span> 1/23, 1/30 and 2/6</li>
        <li><span class="day">Tuesday afternoons:</span> 2/7, 2/14 and 2/21</li>
        <li><span class="day">Wednesday afternoons:</span> 3/8, 3/15 and 3/22</li>
        <li><span class="day">Wednesday evenings:</span> 2/8, 2/15 and 2/22</li>
      </ul>
      <p class="location"><span class="label">LOCATION:</span> Ridgeview Public Schools.</p>
      <p class="location">No fee for RPS leaders.</p>
      <p class="fee"><strong>$150</strong> fee for leaders outside of RPS</p>
    </section>

    <div class="enroll-band">Click here to enroll.&nbsp; Go to www.svboces.org to learn more</div>

    <aside class="testimonials"></aside>
    <div class="testimonials-label">What our participants say..</div>
    <div class="quotes">
      <blockquote>This has been an empowering experience that allowed me to try out dramatic changes in my practice that I wouldn't have imagined before.</blockquote>
      <blockquote>I never realized how often I've guessed and assumed what our teachers and students need &ndash; now I have a way to stop guessing!</blockquote>
      <blockquote>I finally have tools to generate truly creative ideas that people actually embrace&hellip; because they meet their needs.</blockquote>
    </div>
    <div class="contact">
      <p class="org">Summit Valley BOCES</p>
      <p class="web">www.svboces.org</p>
      <p class="ask">Questions?</p>
      <p class="email">j.carter@svboces.org</p>
    </div>
  </article>
</body>
</html>
```